WP website design (Vell)

We need a wordpress design for an established auction and real estate company based in Tennessee. The winning design will incorporate a professional color scheme with company logo in a clean layout. The design needs to consider that this will be developed on a responsive theme. Colors are those that will highlight the logo.

Industry/Entity Type

Real Estate

Font styles to use
Sans Serif

Colors

Designer to choose colors to be used in the design.

Requirements
Must have
• Navigation: 1) Home - with auctions as content as seen at http://quorvibidhouse.com/ 2) Current Auctions 3) Past Auctions 4) Referrals 5) Why Auction 6) About Us 7) Contact Us

Header will have logo, contact info, Social icons (Facebook, Twitter, Youtube) and tagline "Do Well, Ring Vell!' Slideshow (use stock real estate image for image) will be used either in header or content area.

Widgets: Email signup form, Upcoming Auctions, Register for Online Bidding text, testimonials

Footer will have contact info (below) smaller company logo, and the association logos attached.

```html
<!DOCTYPE html>
<html lang="en">
<head>
<meta charset="utf-8">
<title>Vell Realty &amp; Auction LLC</title>
<link rel="stylesheet" href="https://fonts.googleapis.com/css2?family=Open+Sans:wght@400;600;700&family=Roboto+Condensed:wght@400;700&family=Questrial&display=swap">
<style>
:root{
  --green:#6b8a3e;
  --green-dark:#4f6b28;
  --lime:#8cc63f;
  --lime-light:#b5dc6a;
  --text:#333;
  --muted:#666;
  --blue-link:#1f5fa8;
  --orange:#f07d1a;
  --steel:#3c6ea5;
  --bid:#3f9a2e;
  --navy:#0c2440;
  --grey-band:#e4e4e4;
  --white:#fff;
}
*{box-sizing:border-box;margin:0;padding:0}
html,body{width:1200px;height:2736px;overflow:hidden}
body{position:relative;background:var(--white);font-family:"Open Sans",Arial,sans-serif;color:var(--text);font-size:13px}
.abs{position:absolute}

/* header */
.brand{left:100px;top:30px;display:flex;align-items:center;gap:12px}
.brand-square{width:46px;height:46px;background:var(--green)}
.brand-name{font-family:"Roboto Condensed",sans-serif;font-weight:700;font-size:34px;color:var(--green);line-height:1}
.firm{left:158px;top:88px;font-family:"Roboto Condensed",sans-serif;font-size:14px;color:var(--muted);letter-spacing:1px}
.topbar{right:84px;top:12px;display:flex;align-items:center;gap:10px;font-family:"Roboto Condensed",sans-serif;font-weight:700;font-size:15px;color:var(--green)}
.social{display:flex;gap:7px;margin-right:26px}
.social span{width:26px;height:26px;display:block}
.s1{background:#3b5998}.s2{background:#2fa8e0}.s3{background:#d8261f}
.call b{color:var(--text)}
.tagline{right:84px;top:84px;font-family:"Roboto Condensed",sans-serif;font-size:44px;color:#3a3a3a}

/* nav */
.nav{left:0;top:158px;width:1200px;height:44px;background:var(--green);display:flex;align-items:center;padding-left:118px}
.nav a{color:var(--white);text-decoration:none;font-size:14px;height:44px;line-height:44px;padding:0 20px;position:relative}
.nav a.active{background:#1c1c1c;padding:0 34px}
.nav a+a::before{content:"|";position:absolute;left:-3px;color:#d6e3c4}
.nav a.active+a::before{content:none}

/* hero */
.hero{left:0;top:202px;width:1200px;height:470px;background:linear-gradient(90deg,#0b2038 0%,#143b66 4%,var(--navy) 8%,var(--navy) 92%,#1d5b9a 97%,#0b2038 100%)}
.hero-frame{position:absolute;left:88px;top:10px;width:1044px;height:450px;border:5px solid var(--white);background:linear-gradient(180deg,#7fb3e6 0%,#bcd8ef 30%,#9a6a4c 55%,#7e4a32 72%,#5d7b3e 100%)}
.hero-arrow{position:absolute;top:220px}
.hero-box{position:absolute;left:25px;top:85px;width:330px;height:315px;background:rgba(124,180,52,.82);padding:20px 18px;color:var(--white)}
.hero-box h1{font-size:23px;line-height:28px;font-weight:700}
.hero-box p{font-size:11px;line-height:15px;margin-top:8px}
.hero-box .bid-label{margin-top:20px;font-size:12px;font-weight:600}
.hero-box .price{font-size:25px;font-weight:700;margin-top:2px}
.hero-btn{display:inline-block;margin-top:10px;background:#3d3f46;color:var(--white);font-size:18px;padding:9px 16px;border-radius:3px}

/* widgets */
.widget{top:686px;width:330px;height:344px;background:var(--lime);border:1px solid #7fb33a}
.widget h2{font-family:"Questrial",sans-serif;font-size:21px;color:var(--green-dark);height:52px;line-height:52px;padding-left:18px;background:linear-gradient(180deg,#d6eea8,var(--lime-light))}
.widget .photo{margin:12px auto 0;width:266px;height:190px;background:linear-gradient(180deg,#6aa1d8 0%,#c9b79c 50%,#8a7a63 80%,#3d7aa6 100%);border:2px solid #e9f4d6}
.widget .cap{text-align:center;color:var(--white);padding:8px 18px 0}
.widget .cap b{display:block;font-size:12px}
.widget .cap span{font-size:11px;line-height:14px;display:block}
.widget.reg{background:var(--white);border-color:#9ccb5c}
.widget.reg h2{background:var(--white);color:var(--green-dark);text-align:center;padding:0}
.reg-body{background:var(--lime);height:290px;padding:10px 28px}
.reg-body .note{font-size:11px;color:#2d4a12;text-align:center}
.reg-body .field{height:32px;margin-top:10px;background:var(--white);border:1px solid #cfe3ad;font-size:11px;color:#aaa;line-height:30px;padding-left:10px}
.reg-body .submit{margin-top:12px;display:inline-block;background:#2d3a1e;color:var(--white);font-size:14px;padding:5px 14px}
.reg-body .signin{margin-top:10px;font-size:11px;color:#2d4a12}
.reg-body .signin a{color:#14400f;text-decoration:none}

/* auctions */
.section-title{left:95px;top:1055px;font-family:"Questrial",sans-serif;font-size:31px;color:var(--green)}
.pager{display:flex;gap:2px}
.pager span{background:#3a3a3a;color:var(--white);font-size:11px;height:22px;line-height:22px;padding:0 9px}
.pager-top{right:80px;top:1062px}
.pager-bot{right:80px;top:2100px}
.showing{left:95px;top:2110px;font-size:13px;font-weight:700;color:var(--green)}
.grid{left:95px;top:1103px;width:1025px;display:grid;grid-template-columns:502px 502px;grid-auto-rows:318px;column-gap:21px;row-gap:22px}
.card{border:1px solid #d2d2d2;padding:9px}
.card-head{background:var(--green);color:var(--white);font-size:14px;height:36px;line-height:36px;padding-left:10px}
.card-body{display:flex;gap:14px;margin-top:9px}
.card-left{width:234px}
.card-photo{height:100px;background:linear-gradient(180deg,#7eaee0 0%,#d8d8d8 45%,#6c6c6c 65%,#5b9a3a 100%)}
.btn-row{display:flex;gap:6px;margin-top:8px}
.btn{height:32px;color:var(--white);font-size:11px;display:flex;align-items:center;justify-content:space-between;padding:0 6px 0 10px}
.btn.details{background:var(--orange);width:110px}
.btn.video{background:var(--steel);width:118px}
.btn.online{background:var(--bid);width:234px;margin-top:6px}
.card-right{flex:1}
.card-right h3{font-size:15px;line-height:17px;color:var(--green);font-weight:600}
.card-right p{font-size:11px;line-height:15px;color:#555;margin-top:8px}
.card-right hr{border:0;border-top:1px solid #ddd;margin:8px 0}
.card-right h4{font-size:15px;line-height:17px;color:var(--green);font-weight:600}
.meta{font-size:12px;margin-top:8px;line-height:15px}
.meta b{display:block;color:#222}
.meta .date{color:var(--blue-link)}

/* testimonial */
.testi-photo{left:95px;top:2165px;width:243px;height:220px;background:linear-gradient(180deg,#e8e8e8 0%,#cfcfcf 55%,#2c2f36 100%)}
.testi{left:338px;top:2165px;width:782px;height:220px;background:var(--green);padding:28px 26px;color:var(--white)}
.testi .who{font-size:18px}
.testi .who b{font-style:italic}
.testi hr{border:0;border-top:1px solid #a7bf85;margin:14px 0}
.testi p{font-size:14px;line-height:20px}
.testi-nav{position:absolute;right:28px;top:40px;display:flex;gap:3px}
.testi-nav span{width:24px;height:24px;background:#111;display:flex;align-items:center;justify-content:center}

/* newsletter */
.news{left:0;top:2425px;width:1200px;height:105px;background:var(--grey-band)}
.news-text{position:absolute;left:116px;top:40px;display:flex;align-items:center;gap:14px;font-size:16px;color:#444}
.news-input{position:absolute;left:567px;top:30px;width:345px;height:44px;background:var(--white);border:1px solid #ccc;font-size:12px;color:#aaa;line-height:42px;padding-left:12px}
.news-btn{position:absolute;left:930px;top:30px;width:92px;height:44px;background:var(--lime);color:var(--white);font-size:16px;text-align:center;line-height:44px}

/* footer */
.foot-h{font-family:"Roboto Condensed",sans-serif;font-weight:700;font-size:15px;color:var(--green)}
.assoc{left:98px;top:2568px}
.badges{display:flex;gap:10px;margin-top:20px;align-items:center}
.badges span{display:block;background:#2b2b2b}
.contact{left:465px;top:2568px;font-size:12px;line-height:17px;color:#333}
.contact .foot-h{margin-bottom:10px}
.contact a{color:var(--blue-link);text-decoration:none}
.foot-brand{left:630px;top:2600px;display:flex;align-items:center;gap:10px}
.foot-brand .brand-square{width:40px;height:40px}
.foot-brand .brand-name{font-size:29px}
.foot-social{right:80px;top:2568px;text-align:right}
.foot-social .social{justify-content:flex-end;margin:20px 0 0}
.copy{left:95px;top:2678px;font-size:11px;color:#777}
</style>
</head>
<body>

<header>
  <div class="abs brand"><span class="brand-square"></span><span class="brand-name">Vell Realty &amp; Auction LLC</span></div>
  <div class="abs firm">FIRM # 4187</div>
  <div class="abs topbar">
    <span>Get In Touch With Us</span>
    <span class="social" aria-label="Social links"><span class="s1"></span><span class="s2"></span><span class="s3"></span></span>
    <span class="call">Call Us : <b>(800) 555-0147</b></span>
  </div>
  <div class="abs tagline">Do Well, Ring Vell!</div>
</header>

<nav class="abs nav">
  <a class="active">Home</a><a>Current Auctions</a><a>Past Auctions</a><a>Referrals</a><a>Why Auction</a><a>About Us</a><a>Contact Us</a>
</nav>

<section class="abs hero">
  <svg class="hero-arrow" style="left:50px" width="20" height="30" viewBox="0 0 20 30"><path d="M15 3 L4 15 L15 27" stroke="#fff" stroke-width="4" fill="none"/></svg>
  <svg class="hero-arrow" style="left:1150px" width="20" height="30" viewBox="0 0 20 30"><path d="M5 3 L16 15 L5 27" stroke="#fff" stroke-width="4" fill="none"/></svg>
  <div class="hero-frame" role="img" aria-label="Photo of a brick suburban family house with a grey roof and flowering tree">
    <div class="hero-box">
      <h1>Lorem ipsum dolor sit amet, cons ectetur adipiscing elit.</h1>
      <p>Duis aute irure dolor in reprehenderit in voluptate velit esse cillum dolore eu fugiat.</p>
      <div class="bid-label">Est. Opening bid</div>
      <div class="price">$459,054.59</div>
      <span class="hero-btn">View Details</span>
    </div>
  </div>
</section>

<aside class="abs widget" style="left:103px">
  <h2>Upcoming Auctions</h2>
  <div class="photo" role="img" aria-label="Photo of a large modern villa with balconies"></div>
  <div class="cap"><b>Lorem ipsum</b><span>Praesent tibuluma molestie lacuenean udotonmera yhe ndr erit mauris ketyade. Mtayrtyasera ...</span></div>
</aside>

<aside class="abs widget reg" style="left:447px">
  <h2>Register for Online Bidding</h2>
  <div class="reg-body">
    <div class="note">Not yet registerd? Register Now. Just fill in the form.</div>
    <div class="field">Your Name</div>
    <div class="field">Your Email id</div>
    <div class="field">Your Phone No.</div>
    <div class="field">Your Address</div>
    <span class="submit">Submit</span>
    <div class="signin">Already registerd? <a>Sign In</a></div>
  </div>
</aside>

<aside class="abs widget" style="left:788px">
  <h2>Featured Auctions</h2>
  <div class="photo" role="img" aria-label="Photo of a large modern villa with a pool"></div>
  <div class="cap"><b>Lorem ipsum</b><span>Praesent tibuluma molestie lacuenean udotonmera yhe ndr erit mauris ketyade. Mtayrtyasera ...</span></div>
</aside>

<h2 class="abs section-title">Upcoming Auctions</h2>
<div class="abs pager pager-top"><span>1</span><span>2</span><span>Next</span></div>

<main class="abs grid">
  <!-- card template repeated -->
  <article class="card">
    <div class="card-head">Lorem ipsum dolor sit amet conse ctetur adipisicing</div>
    <div class="card-body">
      <div class="card-left">
        <div class="card-photo" role="img" aria-label="Photo of a two-storey house with a lawn"></div>
        <div class="btn-row">
          <span class="btn details">See Details <svg width="20" height="20" viewBox="0 0 20 20"><circle cx="8" cy="8" r="6" stroke="#fff" stroke-width="2" fill="none"/><path d="M12 12 L18 18" stroke="#fff" stroke-width="3"/></svg></span>
          <span class="btn video">See Video <svg width="16" height="18" viewBox="0 0 16 18"><path d="M2 1 L15 9 L2 17Z" fill="#fff"/></svg></span>
        </div>
        <span class="btn online">Click Here for Online Bidding <svg width="22" height="18" viewBox="0 0 22 18"><rect x="1" y="1" width="20" height="12" stroke="#fff" stroke-width="2" fill="none"/><path d="M7 17 H15 M11 13 V17" stroke="#fff" stroke-width="2"/></svg></span>
      </div>
      <div class="card-right">
        <h3>Lorem ipsum dolor sit amet conse ctetur adipiscing</h3>
        <p>Duis aute irure dolor in reprehenderit in voluptate velit esse cillum dolore eu fugiat.</p>
        <hr>
        <h4>Live Off-site Auction with Online Bidding</h4>
        <div class="meta"><b>Begins:</b><span class="date">Tuesday, December 23, 2014 at 1:00 PM EST</span></div>
        <div class="meta"><b>Location:</b>P.O. Box 40512, Brookfield, TN 37001</div>
      </div>
    </div>
  </article>
  <article class="card">
    <div class="card-head">Lorem ipsum dolor sit amet conse ctetur adipisicing</div>
    <div class="card-body">
      <div class="card-left">
        <div class="card-photo" role="img" aria-label="Photo of a two-storey house with a lawn"></div>
        <div class="btn-row">
          <span class="btn details">See Details <svg width="20" height="20" viewBox="0 0 20 20"><circle cx="8" cy="8" r="6" stroke="#fff" stroke-width="2" fill="none"/><path d="M12 12 L18 18" stroke="#fff" stroke-width="3"/></svg></span>
          <span class="btn video">See Video <svg width="16" height="18" viewBox="0 0 16 18"><path d="M2 1 L15 9 L2 17Z" fill="#fff"/></svg></span>
        </div>
        <span class="btn online">Click Here for Online Bidding <svg width="22" height="18" viewBox="0 0 22 18"><rect x="1" y="1" width="20" height="12" stroke="#fff" stroke-width="2" fill="none"/><path d="M7 17 H15 M11 13 V17" stroke="#fff" stroke-width="2"/></svg></span>
      </div>
      <div class="card-right">
        <h3>Lorem ipsum dolor sit amet conse ctetur adipiscing</h3>
        <p>Duis aute irure dolor in reprehenderit in voluptate velit esse cillum dolore eu fugiat.</p>
        <hr>
        <h4>Live Off-site Auction with Online Bidding</h4>
        <div class="meta"><b>Begins:</b><span class="date">Tuesday, December 23, 2014 at 1:00 PM EST</span></div>
        <div class="meta"><b>Location:</b>P.O. Box 40512, Brookfield, TN 37001</div>
      </div>
    </div>
  </article>
  <article class="card">
    <div class="card-head">Lorem ipsum dolor sit amet conse ctetur adipisicing</div>
    <div class="card-body">
      <div class="card-left">
        <div class="card-photo" role="img" aria-label="Photo of a two-storey house with a lawn"></div>
        <div class="btn-row">
          <span class="btn details">See Details <svg width="20" height="20" viewBox="0 0 20 20"><circle cx="8" cy="8" r="6" stroke="#fff" stroke-width="2" fill="none"/><path d="M12 12 L18 18" stroke="#fff" stroke-width="3"/></svg></span>
          <span class="btn video">See Video <svg width="16" height="18" viewBox="0 0 16 18"><path d="M2 1 L15 9 L2 17Z" fill="#fff"/></svg></span>
        </div>
        <span class="btn online">Click Here for Online Bidding <svg width="22" height="18" viewBox="0 0 22 18"><rect x="1" y="1" width="20" height="12" stroke="#fff" stroke-width="2" fill="none"/><path d="M7 17 H15 M11 13 V17" stroke="#fff" stroke-width="2"/></svg></span>
      </div>
      <div class="card-right">
        <h3>Lorem ipsum dolor sit amet conse ctetur adipiscing</h3>
        <p>Duis aute irure dolor in reprehenderit in voluptate velit esse cillum dolore eu fugiat.</p>
        <hr>
        <h4>Live Off-site Auction with Online Bidding</h4>
        <div class="meta"><b>Begins:</b><span class="date">Tuesday, December 23, 2014 at 1:00 PM EST</span></div>
        <div class="meta"><b>Location:</b>P.O. Box 40512, Brookfield, TN 37001</div>
      </div>
    </div>
  </article>
  <article class="card">
    <div class="card-head">Lorem ipsum dolor sit amet conse ctetur adipisicing</div>
    <div class="card-body">
      <div class="card-left">
        <div class="card-photo" role="img" aria-label="Photo of a two-storey house with a lawn"></div>
        <div class="btn-row">
          <span class="btn details">See Details <svg width="20" height="20" viewBox="0 0 20 20"><circle cx="8" cy="8" r="6" stroke="#fff" stroke-width="2" fill="none"/><path d="M12 12 L18 18" stroke="#fff" stroke-width="3"/></svg></span>
          <span class="btn video">See Video <svg width="16" height="18" viewBox="0 0 16 18"><path d="M2 1 L15 9 L2 17Z" fill="#fff"/></svg></span>
        </div>
        <span class="btn online">Click Here for Online Bidding <svg width="22" height="18" viewBox="0 0 22 18"><rect x="1" y="1" width="20" height="12" stroke="#fff" stroke-width="2" fill="none"/><path d="M7 17 H15 M11 13 V17" stroke="#fff" stroke-width="2"/></svg></span>
      </div>
      <div class="card-right">
        <h3>Lorem ipsum dolor sit amet conse ctetur adipiscing</h3>
        <p>Duis aute irure dolor in reprehenderit in voluptate velit esse cillum dolore eu fugiat.</p>
        <hr>
        <h4>Live Off-site Auction with Online Bidding</h4>
        <div class="meta"><b>Begins:</b><span class="date">Tuesday, December 23, 2014 at 1:00 PM EST</span></div>
        <div class="meta"><b>Location:</b>P.O. Box 40512, Brookfield, TN 37001</div>
      </div>
    </div>
  </article>
  <article class="card">
    <div class="card-head">Lorem ipsum dolor sit amet conse ctetur adipisicing</div>
    <div class="card-body">
      <div class="card-left">
        <div class="card-photo" role="img" aria-label="Photo of a two-storey house with a lawn"></div>
        <div class="btn-row">
          <span class="btn details">See Details <svg width="20" height="20" viewBox="0 0 20 20"><circle cx="8" cy="8" r="6" stroke="#fff" stroke-width="2" fill="none"/><path d="M12 12 L18 18" stroke="#fff" stroke-width="3"/></svg></span>
          <span class="btn video">See Video <svg width="16" height="18" viewBox="0 0 16 18"><path d="M2 1 L15 9 L2 17Z" fill="#fff"/></svg></span>
        </div>
        <span class="btn online">Click Here for Online Bidding <svg width="22" height="18" viewBox="0 0 22 18"><rect x="1" y="1" width="20" height="12" stroke="#fff" stroke-width="2" fill="none"/><path d="M7 17 H15 M11 13 V17" stroke="#fff" stroke-width="2"/></svg></span>
      </div>
      <div class="card-right">
        <h3>Lorem ipsum dolor sit amet conse ctetur adipiscing</h3>
        <p>Duis aute irure dolor in reprehenderit in voluptate velit esse cillum dolore eu fugiat.</p>
        <hr>
        <h4>Live Off-site Auction with Online Bidding</h4>
        <div class="meta"><b>Begins:</b><span class="date">Tuesday, December 23, 2014 at 1:00 PM EST</span></div>
        <div class="meta"><b>Location:</b>P.O. Box 40512, Brookfield, TN 37001</div>
      </div>
    </div>
  </article>
  <article class="card">
    <div class="card-head">Lorem ipsum dolor sit amet conse ctetur adipisicing</div>
    <div class="card-body">
      <div class="card-left">
        <div class="card-photo" role="img" aria-label="Photo of a two-storey house with a lawn"></div>
        <div class="btn-row">
          <span class="btn details">See Details <svg width="20" height="20" viewBox="0 0 20 20"><circle cx="8" cy="8" r="6" stroke="#fff" stroke-width="2" fill="none"/><path d="M12 12 L18 18" stroke="#fff" stroke-width="3"/></svg></span>
          <span class="btn video">See Video <svg width="16" height="18" viewBox="0 0 16 18"><path d="M2 1 L15 9 L2 17Z" fill="#fff"/></svg></span>
        </div>
        <span class="btn online">Click Here for Online Bidding <svg width="22" height="18" viewBox="0 0 22 18"><rect x="1" y="1" width="20" height="12" stroke="#fff" stroke-width="2" fill="none"/><path d="M7 17 H15 M11 13 V17" stroke="#fff" stroke-width="2"/></svg></span>
      </div>
      <div class="card-right">
        <h3>Lorem ipsum dolor sit amet conse ctetur adipiscing</h3>
        <p>Duis aute irure dolor in reprehenderit in voluptate velit esse cillum dolore eu fugiat.</p>
        <hr>
        <h4>Live Off-site Auction with Online Bidding</h4>
        <div class="meta"><b>Begins:</b><span class="date">Tuesday, December 23, 2014 at 1:00 PM EST</span></div>
        <div class="meta"><b>Location:</b>P.O. Box 40512, Brookfield, TN 37001</div>
      </div>
    </div>
  </article>
</main>

<div class="abs showing">Showing 4 of 20 results</div>
<div class="abs pager pager-bot"><span>1</span><span>2</span><span>Next</span></div>

<div class="abs testi-photo" role="img" aria-label="Portrait photo of a customer in a suit"></div>
<section class="abs testi">
  <div class="who"><b>Owen Harlow,</b> Customer</div>
  <div class="testi-nav">
    <span><svg width="10" height="12" viewBox="0 0 10 12"><path d="M8 1 L2 6 L8 11" stroke="#fff" stroke-width="2.5" fill="none"/></svg></span>
    <span><svg width="10" height="12" viewBox="0 0 10 12"><path d="M2 1 L8 6 L2 11" stroke="#fff" stroke-width="2.5" fill="none"/></svg></span>
  </div>
  <hr>
  <p>Lorem ipsum dolor sit amet consectetuer adipiscing elit. Praesent vestibulum molestie lacus. Aenean nonummy hendrerit mauscipit varius mi. Cum sociis natoque penatibus nis dis parturient montes nascetur ridiculus mus. Nulla dui. Donec aisuadicnc sit amet eros. Lorem ipsum dolor sit at consc tetuer aiing elituris fermentum turned laoor wenai...</p>
</section>

<section class="abs news">
  <div class="news-text">
    <svg width="30" height="22" viewBox="0 0 30 22"><rect x="1" y="1" width="28" height="20" fill="#6b8a3e"/><path d="M1 1 L15 12 L29 1" stroke="#fff" stroke-width="2" fill="none"/></svg>
    Subscribe To Our Newsletter for weekly and monthly
  </div>
  <div class="news-input">Type your email id</div>
  <div class="news-btn">Submit</div>
</section>

<footer>
  <div class="abs assoc">
    <div class="foot-h">Our Associates</div>
    <div class="badges" aria-label="Association badges">
      <span style="width:78px;height:30px"></span>
      <span style="width:44px;height:36px"></span>
      <span style="width:98px;height:34px"></span>
      <span style="width:40px;height:40px"></span>
    </div>
  </div>
  <div class="abs contact">
    <div class="foot-h">Contact Us</div>
    Unit 8, Suite No 14<br>Larkin Street<br>Maple Grove<br>Tennessee<br>
    Email: <a>info@vellrealty.com</a><br>
    Website: <a>www.vellrealty.com</a>
  </div>
  <div class="abs foot-brand"><span class="brand-square"></span><span class="brand-name">Vell Realty &amp; Auction LLC</span></div>
  <div class="abs foot-social">
    <div class="foot-h">Get In Touch With Us</div>
    <div class="social"><span class="s1"></span><span class="s2"></span><span class="s3"></span></div>
  </div>
  <div class="abs copy">© 2014, All Rights Reserved</div>
</footer>

</body>
</html>
```